WordPress Design for both website and landing page for an expert

I need a clean and stylish design for my new website. I work as an expert (see attached file WHY HOW WHAT), my product is expert opinion (reports) for company evaluations You can use all of the attached pictures colored or black / white. The person is me, you can add other pictures, if you want. The design should be clean and stylish, so you could use white, black, gray, silver and / or one additional color. I have added an idea about my website, see attached file CONCEPT WEBSITE If you have any more information, please do not hesitate to contact us 'Hesitate to ask me ...

```html
<!DOCTYPE html>
<html lang="en">
<head>
<meta charset="utf-8">
<title>Lukas Verhoeven – Expert for Company Valuations</title>
<link href="https://fonts.googleapis.com/css2?family=Lato:ital,wght@0,300;0,400;0,700;1,300;1,400&family=Oswald:wght@300;400;500&display=swap" rel="stylesheet">
<style>
:root{
  --accent:#2aa7d8;
  --accent-strong:#1a9be6;
  --note:#2a8fd0;
  --ink:#333333;
  --muted:#8a8a8a;
  --light-bg:#f5f5f5;
  --card-bg:#eeeeee;
  --dark:#1e1f21;
  --footer:#2b2b2b;
  --white:#ffffff;
}
*{box-sizing:border-box;margin:0;padding:0}
html,body{width:1200px;height:2429px;overflow:hidden}
body{position:relative;background:var(--white);font-family:'Lato',sans-serif;color:var(--ink)}
.abs{position:absolute}

/* header */
.site-header{position:absolute;left:0;top:0;width:1200px;height:113px;background:var(--white)}
.brand{position:absolute;left:62px;top:40px;display:flex;align-items:center;gap:12px;font-family:'Oswald',sans-serif;font-weight:400;font-size:25px;letter-spacing:3px;color:#6b6b6b}
.brand-dot{width:22px;height:22px;border-radius:50%;background:#6b6b6b}
.nav{position:absolute;top:46px;left:0;width:1200px;font-family:'Oswald',sans-serif;font-weight:300;font-size:16px;color:#555}
.nav a{position:absolute;color:inherit;text-decoration:none;white-space:nowrap}
.nav a.is-active{color:var(--accent)}

/* hero */
.hero{position:absolute;left:0;top:113px;width:1200px;height:607px;overflow:hidden;
  background:linear-gradient(180deg,#5f8f9a 0%,#8fb3b3 35%,#9fb2a6 50%,#5a4b3f 68%,#3b2e26 85%,#2a231f 100%)}
.hero-person{position:absolute;left:777px;top:65px;width:356px;height:542px;
  background:linear-gradient(180deg,#d9b9a6 0%,#c7a08a 18%,#4a4d52 30%,#3a3c40 100%);border-radius:150px 150px 0 0}
.hero-curve{position:absolute;left:0;bottom:0}
.hero-title-box{position:absolute;left:65px;top:255px;width:707px;height:126px;background:rgba(60,80,80,.55);padding:18px 30px}
.hero-title{font-family:'Oswald',sans-serif;font-weight:400;font-size:46px;line-height:1.05;color:var(--white);letter-spacing:1px}
.hero-url{font-family:'Oswald',sans-serif;font-weight:300;font-size:21px;letter-spacing:3px;color:var(--white);margin-top:2px}

/* why */
.why{position:absolute;left:0;top:720px;width:1200px;height:481px;background:var(--light-bg)}
.section-title{position:absolute;left:0;width:1200px;text-align:center;font-weight:700;font-size:23px;color:var(--ink)}
.section-rule{position:absolute;left:576px;width:48px;height:3px;background:var(--accent)}
.section-sub{position:absolute;left:0;width:1200px;text-align:center;font-style:italic;font-weight:300;font-size:15px;color:#666}
.card{position:absolute;top:242px;height:213px;background:var(--card-bg);text-align:center;padding:0 24px}
.card svg{position:absolute;left:50%;top:30px;transform:translateX(-50%)}
.card-title{position:absolute;left:0;top:93px;width:100%;font-weight:700;font-size:15px;color:#222}
.card-text{position:absolute;left:24px;right:24px;top:122px;font-weight:300;font-size:12.5px;line-height:1.5;color:var(--muted)}

/* motives */
.motives-photo{position:absolute;left:100px;top:1294px;width:361px;height:344px;
  background:linear-gradient(135deg,#4a5360 0%,#c9ccd1 40%,#e9ecef 60%,#2f7fc4 100%)}
.motives-title{position:absolute;left:544px;top:1312px;font-weight:700;font-size:21px;color:#222}
.motive-list{position:absolute;left:555px;top:1368px;list-style:none;font-size:13px;color:#333}
.motive-list li{display:flex;align-items:center;gap:14px;height:33px}
.motive-quote{position:absolute;left:583px;top:1486px;width:500px;font-style:italic;font-size:17px;line-height:1.35;color:#333}
.motive-note{position:absolute;left:559px;top:1566px;width:540px;font-weight:700;font-size:12.5px;line-height:1.8;color:var(--note)}

/* contact */
.contact{position:absolute;left:0;top:1716px;width:1200px;height:632px;
  background:radial-gradient(ellipse at 60% 40%,#3a3b3e 0%,#26272a 55%,var(--dark) 100%)}
.contact .section-title{color:var(--white)}
.contact-intro{position:absolute;left:0;top:1823px;width:1200px;text-align:center;font-style:italic;font-size:13.5px;line-height:1.65;color:#e6e6e6}
.field{position:absolute;border-bottom:1px solid #8c8c8c;display:flex;align-items:center;gap:12px;padding-left:2px;font-size:14px;color:#e0e0e0}
.send-btn{position:absolute;left:512px;top:2142px;width:128px;height:32px;background:var(--accent-strong);color:var(--white);font-weight:700;font-size:11.5px;display:flex;align-items:center;justify-content:center;letter-spacing:.3px}
.info{position:absolute;top:2238px;width:360px;text-align:center;color:var(--white)}
.info svg{display:block;margin:0 auto 10px}
.info-label{font-weight:700;font-size:13px;margin-bottom:6px}
.info-line{font-size:12.5px;line-height:1.7}
.to-top{position:absolute;left:1143px;top:2284px;width:37px;height:38px;background:#4fb6ea}

/* footer */
.site-footer{position:absolute;left:0;top:2348px;width:1200px;height:81px;background:var(--footer)}
.copyright{position:absolute;left:55px;top:34px;font-weight:700;font-size:11.5px;color:var(--white)}
.social{position:absolute;left:921px;top:30px;display:flex;gap:19px}
.social span{width:18px;height:18px;border-radius:50%;background:var(--white)}
</style>
</head>
<body>

<header class="site-header">
  <div class="brand"><span class="brand-dot"></span>LUKAS VERHOEVEN</div>
  <nav class="nav">
    <a class="is-active" style="left:599px">HOME</a>
    <a style="left:673px">WHAT I DO</a>
    <a style="left:777px">WHY &amp; HOW I DO</a>
    <a style="left:929px">ABOUT ME</a>
    <a style="left:1036px">CONTACT</a>
  </nav>
</header>

<section class="hero" role="img" aria-label="Evening city skyline with a tall TV tower under a cloudy sky">
  <div class="hero-person" role="img" aria-label="Portrait of the valuation expert in a grey suit"></div>
  <div class="hero-title-box">
    <h1 class="hero-title">EXPERT FOR COMPANY VALUATIONS</h1>
    <p class="hero-url">www.verhoeven-valuation.de</p>
  </div>
  <svg class="hero-curve" width="1200" height="120" viewBox="0 0 1200 120">
    <path d="M420 120 C700 110 1000 75 1200 30 L1200 120 Z" fill="#f5f5f5"/>
  </svg>
</section>

<section class="why">
  <h2 class="section-title" style="top:86px">WHY WORK WITH ME?</h2>
  <div class="section-rule" style="top:127px"></div>
  <p class="section-sub" style="top:150px">3 reasons, why you should work with me...</p>

  <div class="card" style="left:89px;width:316px">
    <svg width="64" height="50" viewBox="0 0 64 50" fill="none" stroke="#2aa7d8" stroke-width="3" stroke-linecap="round">
      <circle cx="44" cy="8" r="5" fill="#2aa7d8"/>
      <path d="M24 16 L40 16 L34 30 L44 38 L40 48 M34 30 L22 36 L16 46 M40 16 L50 24 L58 20"/>
      <path d="M2 20 H16 M6 28 H18 M2 36 H12"/>
    </svg>
    <h3 class="card-title">FAST</h3>
    <p class="card-text">You will receive your report promptly (within a maximum of 21 days after receipt of all required documents)</p>
  </div>
  <div class="card" style="left:434px;width:322px">
    <svg width="50" height="56" viewBox="0 0 50 56" fill="none" stroke="#2aa7d8" stroke-width="2">
      <circle cx="25" cy="22" r="18"/><circle cx="25" cy="22" r="12"/>
      <path d="M19 22 l4 4 l8 -8"/><path d="M14 36 L10 54 L18 48 L22 54 L25 40 L28 54 L32 48 L40 54 L36 36"/>
    </svg>
    <h3 class="card-title">CERTIFIED</h3>
    <p class="card-text">You receive a qualified and reliable report from a certified expert (highest acceptance by all parties)</p>
  </div>
  <div class="card" style="left:784px;width:323px">
    <svg width="54" height="58" viewBox="0 0 54 58" fill="none" stroke="#2aa7d8" stroke-width="2">
      <path d="M14 54 V40 C6 34 6 18 16 12 C28 4 46 12 44 28 L48 36 H43 V46 H34 V54"/>
      <circle cx="28" cy="26" r="8"/><circle cx="28" cy="26" r="3"/>
      <path d="M27 2 V8 M12 6 l4 5 M42 6 l-4 5 M4 18 l6 2 M50 18 l-6 2"/>
    </svg>
    <h3 class="card-title">UNDERSTANDABLE</h3>
    <p class="card-text">Your report will be logical and comprehensible for you and will not contain any "technical Chinese"</p>
  </div>
</section>

<div class="motives-photo" role="img" aria-label="Business people reviewing a printed bar chart report with a pen"></div>
<h2 class="motives-title">WHAT ARE THE BUYING MOTIVES OF THE CUSTOMERS?</h2>
<ul class="motive-list">
  <li><svg width="10" height="10" viewBox="0 0 10 10"><path d="M1 5 l3 3 l5 -7" stroke="#333" stroke-width="1.6" fill="none"/></svg>You want to sell shares of your company or your entire company?</li>
  <li><svg width="10" height="10" viewBox="0 0 10 10"><path d="M1 5 l3 3 l5 -7" stroke="#333" stroke-width="1.6" fill="none"/></svg>You want to transfer your business to your heirs and need a valuation for the tax office?</li>
  <li><svg width="10" height="10" viewBox="0 0 10 10"><path d="M1 5 l3 3 l5 -7" stroke="#333" stroke-width="1.6" fill="none"/></svg>You have to pay someone in the context of a separation / divorce and need a tax base?</li>
</ul>
<p class="motive-quote">Have your company evaluated by a qualified expert and avoid many (unnecessary) quarrels.</p>
<p class="motive-note">Note: The cost of a report are always disproportionately cheaper than the cost of legal disputes. And that detached from the psychological burden of such an argument ...</p>

<section class="contact" role="img" aria-label="Dark desk with a tablet, keyboard and mouse">
  <h2 class="section-title" style="top:36px">CONTACT US</h2>
  <div class="section-rule" style="top:78px"></div>
</section>
<p class="contact-intro">Lorem ipsum dolor sit amet, no mollis regione accusamus qui. Legere voluptua mei an,<br>passim aliquid utroque et ius, molestie maksu rez id sea.</p>

<div class="field" style="left:278px;top:1908px;width:292px;height:30px">
  <svg width="14" height="14" viewBox="0 0 14 14" fill="#e0e0e0"><circle cx="7" cy="4" r="3.2"/><path d="M1 14 C1 8 13 8 13 14 Z"/></svg>Name
</div>
<div class="field" style="left:599px;top:1908px;width:295px;height:30px">
  <svg width="14" height="14" viewBox="0 0 14 14" fill="none" stroke="#e0e0e0" stroke-width="1.4"><path d="M1 7 L13 1 L9 13 L7 8 Z"/></svg>
</div>
<div class="field" style="left:278px;top:1988px;width:616px;height:101px;align-items:flex-start;padding-top:4px">
  <svg width="15" height="12" viewBox="0 0 15 12" fill="none" stroke="#e0e0e0" stroke-width="1.4"><rect x="1" y="1" width="13" height="10"/><path d="M1 1 L7.5 7 L14 1"/></svg>Message
</div>
<div class="send-btn">SEND MESSAGE</div>

<div class="info" style="left:55px">
  <svg width="14" height="18" viewBox="0 0 14 18" fill="#fff"><path d="M7 0 C3 0 0 3 0 7 C0 12 7 18 7 18 C7 18 14 12 14 7 C14 3 11 0 7 0 Z"/><circle cx="7" cy="7" r="2.5" fill="#26272a"/></svg>
  <p class="info-label">OUR LOCATION</p>
  <p class="info-line">1420 Harbor Lane, Westfield<br>CA 90210, Australia</p>
</div>
<div class="info" style="left:406px">
  <svg width="16" height="16" viewBox="0 0 16 16" fill="#fff"><path d="M3 1 L6 1 L7 5 L5 6.5 C6 9 7 10 9.5 11 L11 9 L15 10 L15 13 C15 14 14 15 13 15 C6 15 1 10 1 3 C1 2 2 1 3 1 Z"/></svg>
  <p class="info-label">CALL US</p>
  <p class="info-line">+ 1 555 010 2847<br>+ 1 555 010 2873</p>
</div>
<div class="info" style="left:756px">
  <svg width="18" height="14" viewBox="0 0 18 14" fill="none" stroke="#fff" stroke-width="1.6"><rect x="1" y="1" width="16" height="12" rx="1"/><path d="M1 1 L9 8 L17 1"/></svg>
  <p class="info-label">YOUR MESSAGE</p>
  <p class="info-line">info@northmere.com<br>admin@northmere.com</p>
</div>
<div class="to-top"><svg width="37" height="38" viewBox="0 0 37 38"><path d="M14 21 l4.5 -4.5 l4.5 4.5" stroke="#fff" stroke-width="1.8" fill="none"/></svg></div>

<footer class="site-footer">
  <p class="copyright">Copyright© 2019 Lukas Verhoeven All Rights Reserved.</p>
  <div class="social" aria-label="Social media links">
    <span></span><span></span><span></span><span></span><span></span>
  </div>
</footer>

</body>
</html>
```